Web Header Banner

I require a web header banner for a website about the cloud.
The banner should be modern, and look professional. And not contain real clouds.
This will be say 'Confused about The Cloud ?
The background will be blue #3399ff and it should be aim for IT professionals.

Target Market(s)

IT Professionals

Industry/Entity Type

It Professional

Requirements
Must have
• Be modern. Not cartoony
Nice to have
• A women looking confused
• Various line pictures of cloud object above head.
• In a ligter blue then the main background. Much like the background to quillnest.
• https://www.quillnest-example.com/business
• Must contain the wording.... Confused about The Cloud?
Should not have
• real life clouds

```html
<!DOCTYPE html>
<html lang="en">
<head>
<meta charset="utf-8">
<title>Confused about The Cloud? – Header Banner</title>
<link rel="stylesheet" href="https://fonts.googleapis.com/css2?family=Nunito:wght@800&display=swap">
<style>
  :root {
    --banner-blue: #4f8fcd;
    --headline-white: #ffffff;
    --badge-white: #ffffff;
    --brand-blue: #3a8fd6;
    --photo-skin: #d9b39a;
    --photo-shirt: #eef0f2;
    --photo-denim: #1f2a3e;
  }
  html, body {
    margin: 0;
    padding: 0;
    width: 1200px;
    height: 303px;
    overflow: hidden;
    background: var(--banner-blue);
  }
  .banner {
    position: relative;
    width: 1200px;
    height: 303px;
    background: var(--banner-blue);
    font-family: "Nunito", "Arial Rounded MT Bold", sans-serif;
    overflow: hidden;
  }
  .banner__photo {
    position: absolute;
    left: 36px;
    top: 0;
    width: 332px;
    height: 303px;
    background: linear-gradient(180deg,
      var(--banner-blue) 0%,
      var(--photo-skin) 18%,
      var(--photo-shirt) 45%,
      var(--photo-shirt) 68%,
      var(--photo-denim) 82%,
      var(--photo-denim) 100%);
    border-radius: 150px 150px 24px 24px;
    opacity: 0.9;
  }
  .banner__headline {
    position: absolute;
    left: 380px;
    top: 112px;
    width: 660px;
    margin: 0;
    text-align: center;
    color: var(--headline-white);
    font-weight: 800;
    font-size: 73px;
    line-height: 84px;
    letter-spacing: 0.5px;
  }
  .brand-badge {
    position: absolute;
    right: 0;
    bottom: 0;
    width: 140px;
    height: 55px;
    background: var(--badge-white);
    display: flex;
    align-items: center;
    justify-content: center;
    gap: 7px;
  }
  .brand-badge__dot {
    width: 16px;
    height: 16px;
    border-radius: 50%;
    background: var(--brand-blue);
  }
  .brand-badge__name {
    color: var(--brand-blue);
    font-weight: 800;
    font-size: 18px;
  }
</style>
</head>
<body>
  <header class="banner">
    <div class="banner__photo" role="img" aria-label="Woman sitting cross-legged with a laptop, shrugging with a confused look"></div>
    <h1 class="banner__headline">Confused about<br>The Cloud ?</h1>
    <div class="brand-badge">
      <span class="brand-badge__dot"></span>
      <span class="brand-badge__name">skyclear</span>
    </div>
  </header>
</body>
</html>
```